Need Business Card for our Real Estate Business with Sales Executive's Picture

PANTONE 484 C ( RED)

PANTONE 2766 C ( BLUE

Industry/Entity Type

Real Estate

Contact Information for Business Card

Name, Mobile, email, & picture of Person
Agency Phone, address, Web address

Requirements
Must have
• Our Logo Colours, Agent Picture,

```html
<!DOCTYPE html>
<html lang="en">
<head>
<meta charset="utf-8">
<title>Mesa Ridge Realty – Business Card</title>
<link rel="stylesheet" href="https://fonts.googleapis.com/css2?family=Open+Sans:ital,wght@0,400;0,600;0,700;1,400;1,700&display=swap">
<style>
  :root {
    --page-bg: #3a3a3c;
    --card-black: #1e1e20;
    --card-edge: #2a2a2d;
    --brand-blue: #162a6e;
    --brand-red: #a3262a;
    --text-light: #f2f2f2;
    --text-muted: #c9c9cc;
    --logo-grey: #4a4a4e;
    --photo-top: #8a93a8;
    --photo-bottom: #2c4c9c;
  }
  * { margin: 0; padding: 0; box-sizing: border-box; }
  html, body {
    width: 799px; height: 1200px; overflow: hidden;
    background: var(--page-bg);
    font-family: "Open Sans", Arial, sans-serif;
  }
  .canvas { position: relative; width: 799px; height: 1200px; }

  .card {
    position: absolute; left: 80px; width: 640px; height: 366px;
    background: var(--card-black);
    border-radius: 6px;
    overflow: hidden;
    box-shadow: 0 12px 30px rgba(0,0,0,.45);
  }
  .card--front { top: 100px; }
  .card--back  { top: 680px; }

  /* Front */
  .front-brand {
    position: absolute; left: 0; right: 0; top: 130px;
    text-align: center;
    color: var(--logo-grey);
    font-size: 34px; font-weight: 700; letter-spacing: 6px;
  }
  .front-brand .mark {
    display: inline-block; width: 14px; height: 14px;
    background: var(--logo-grey); margin-right: 14px; vertical-align: middle;
  }
  .front-web {
    position: absolute; left: 0; right: 0; bottom: 56px;
    display: flex; align-items: center; justify-content: center; gap: 18px;
    color: var(--text-light); font-size: 17px; letter-spacing: .5px;
  }
  .front-web .rule { width: 60px; height: 3px; background: var(--brand-red); }

  /* Back */
  .back-band { position: absolute; inset: 0; }
  .agent {
    position: absolute; left: 40px; top: 34px; color: var(--text-light);
  }
  .agent-name { font-size: 21px; font-weight: 700; font-style: italic; }
  .agent-role { font-size: 14px; font-style: italic; color: var(--text-muted); }
  .agent-photo {
    position: absolute; left: 0; top: 150px; width: 230px; height: 216px;
    background: linear-gradient(180deg, var(--photo-top), var(--photo-bottom));
  }
  .back-brand {
    position: absolute; left: 300px; top: 150px; width: 300px;
    color: var(--text-light); text-align: center;
    font-size: 36px; font-weight: 400; letter-spacing: 5px;
  }
  .back-brand .mark {
    display: inline-block; width: 10px; height: 10px;
    background: var(--text-light); margin-right: 10px; vertical-align: middle;
  }
  .contact {
    position: absolute; left: 310px; top: 218px;
    list-style: none; color: var(--text-light); font-size: 15px; line-height: 22px;
  }
  .contact li { display: flex; align-items: center; gap: 10px; }
  .contact .address { padding-left: 22px; }
  .contact svg { width: 12px; height: 12px; fill: var(--brand-red); flex: none; }
</style>
</head>
<body>
<main class="canvas">

  <section class="card card--front" aria-label="Card front">
    <div class="front-brand"><span class="mark"></span>MESA RIDGE REALTY</div>
    <div class="front-web">
      <span class="rule"></span>
      <span>www.mesaridgerealty.com</span>
      <span class="rule"></span>
    </div>
  </section>

  <section class="card card--back" aria-label="Card back">
    <svg class="back-band" viewBox="0 0 640 366" preserveAspectRatio="none" aria-hidden="true">
      <path d="M0 22 L640 150 L640 200 L420 178 L300 165 L220 150 L0 150 Z" fill="var(--brand-blue)"/>
    </svg>
    <div class="agent">
      <div class="agent-name">Laura Whitfield</div>
      <div class="agent-role">Managing Director</div>
    </div>
    <div class="agent-photo" role="img" aria-label="Portrait photo of the agent in a blue suit"></div>
    <div class="back-brand"><span class="mark"></span>MESA RIDGE</div>
    <ul class="contact">
      <li class="address">418 Cedar Ave #2210,</li>
      <li class="address">Brookfield, CO 80412</li>
      <li><svg viewBox="0 0 12 12"><path d="M2 1h3l1 3-2 1a6 6 0 003 3l1-2 3 1v3c-6 1-10-3-9-9z"/></svg>555.214.3087</li>
      <li><svg viewBox="0 0 12 12"><rect x="3" y="0" width="6" height="12" rx="1"/></svg>555-309-7741</li>
      <li><svg viewBox="0 0 12 12"><path d="M0 2h12v8H0z M0 2l6 5 6-5" stroke="#1e1e20" stroke-width=".8"/></svg>lwhitfield@mesaridgerealty.com</li>
      <li><svg viewBox="0 0 12 12"><circle cx="6" cy="6" r="6"/></svg>www.mesaridgerealty.com</li>
    </ul>
  </section>

</main>
</body>
</html>
```